Modern & Fresh Sumeray Book Cover

Need a creative e-book cover for my book.

Title: Get Sumeray Sorted
Subtitle: Learn How To Easily Choose & Enroll in the Perfect Coverage at the Perfect Time.

Target Market(s)

60-70 year olds in the United States

Font styles to use
Sans Serif

Colors
9bcb3c
33a6d7

Requirements
Must have
• Must look modern and fresh.
• Use our company colors www.BrovaMint.com

```html
<!DOCTYPE html>
<html lang="en">
<head>
<meta charset="utf-8">
<title>Get Sumeray Sorted – Book Cover</title>
<link rel="stylesheet" href="https://fonts.googleapis.com/css2?family=Oswald:wght@700&family=Montserrat:wght@500;700&display=swap">
<style>
  :root {
    --stage: #e9eef2;
    --cover: #eeeeee;
    --cover-edge: #e2e2e2;
    --green-light: #a6cf5a;
    --green: #9bcb3c;
    --green-dark: #6fa23a;
    --blue-light: #33b4d4;
    --blue: #33a6d7;
    --blue-dark: #2a5fa8;
    --band: #1f95ba;
    --band-dark: #177f9f;
    --band-text: #e9f6fa;
  }
  * { box-sizing: border-box; margin: 0; padding: 0; }
  html, body {
    width: 1200px;
    height: 797px;
    overflow: hidden;
    background: var(--stage);
  }
  .canvas {
    position: relative;
    width: 1200px;
    height: 797px;
  }
  .cover {
    position: absolute;
    left: 350px;
    top: 28px;
    width: 500px;
    height: 741px;
    background: var(--cover);
    box-shadow: 0 10px 30px rgba(40, 60, 80, 0.18);
    overflow: hidden;
  }
  .cover-texture {
    position: absolute;
    inset: 0;
    background: linear-gradient(160deg, #f1f1f1 0%, var(--cover-edge) 100%);
  }
  .brand {
    position: absolute;
    top: 78px;
    left: 0;
    width: 100%;
    display: flex;
    justify-content: center;
    align-items: center;
    gap: 10px;
  }
  .brand-dot {
    width: 16px;
    height: 16px;
    border-radius: 50%;
    background: var(--green);
  }
  .brand-name {
    font-family: "Montserrat", sans-serif;
    font-weight: 700;
    font-size: 44px;
    letter-spacing: 0.5px;
    color: var(--green);
  }
  .title {
    position: absolute;
    top: 168px;
    left: 0;
    width: 100%;
    text-align: center;
    font-family: "Oswald", sans-serif;
    font-weight: 700;
    text-transform: uppercase;
    line-height: 0.98;
  }
  .title-line {
    display: block;
    -webkit-background-clip: text;
    background-clip: text;
    color: transparent;
  }
  .title-line--top {
    font-size: 118px;
    background-image: linear-gradient(90deg, var(--green-light), var(--green-dark));
  }
  .title-line--middle {
    font-size: 112px;
    letter-spacing: 1px;
    background-image: linear-gradient(90deg, var(--blue-light), var(--blue) 45%, var(--blue-dark));
  }
  .title-line--bottom {
    font-size: 118px;
    background-image: linear-gradient(90deg, var(--green-light), var(--green-dark));
  }
  .subtitle-band {
    position: absolute;
    left: 0;
    top: 596px;
    width: 100%;
    height: 98px;
    background: linear-gradient(90deg, var(--band), var(--band-dark));
    border-top: 3px solid var(--green);
    border-bottom: 3px solid var(--green);
    box-shadow: 0 -6px 0 -3px var(--cover), 0 6px 0 -3px var(--cover);
    display: flex;
    align-items: center;
    justify-content: center;
    padding: 0 34px;
  }
  .subtitle {
    font-family: "Montserrat", sans-serif;
    font-weight: 500;
    font-size: 15.5px;
    line-height: 1.55;
    letter-spacing: 1.6px;
    text-transform: uppercase;
    text-align: center;
    color: var(--band-text);
  }
</style>
</head>
<body>
<main class="canvas">
  <section class="cover">
    <div class="cover-texture" role="img" aria-label="Faint repeating pattern of medical crosses, pills and clipboards"></div>
    <header class="brand">
      <span class="brand-dot"></span>
      <span class="brand-name">BrovaMint</span>
    </header>
    <h1 class="title">
      <span class="title-line title-line--top">Get</span>
      <span class="title-line title-line--middle">Sumeray</span>
      <span class="title-line title-line--bottom">Sorted</span>
    </h1>
    <div class="subtitle-band">
      <p class="subtitle">Learn how to easily choose &amp; enroll in the perfect coverage at the perfect time</p>
    </div>
  </section>
</main>
</body>
</html>
```